Business card and stationery concept for weight management and nutrition practice
trueLeaf Guidance
Dear Designers,
I have uploaded my logo files and am looking forward to everyone's designs.
I would like to see designs that do not feature my logo quite so prominently - that is, the logo does not have to be very large.
Also, instead of bold abstract curves and shapes I'd like to see accents that are more feminine.
Thanks everyone!
I like the bold concepts you have uploaded. I would also like to see more simple ideas, using the light blue and dark grey used in the logo rather than black.
I would also like to see a few concepts that are a bit more feminine. Not overtly so but subtle.
Thank you!
I am unable to upload my logo at this time -- I will do this on Saturday evening when I get back in town.

```html
<!DOCTYPE html>
<html lang="en">
<head>
<meta charset="utf-8">
<title>trueLeaf Guidance – Business Card</title>
<link href="https://fonts.googleapis.com/css2?family=Open+Sans:wght@400;600;700&display=swap" rel="stylesheet">
<style>
  :root {
    --page-bg: #e9eaec;
    --card-white: #ffffff;
    --ink-dark: #3a3c40;
    --ink-mid: #6b6e73;
    --band-dark: #2f3033;
    --band-light: #5a5c60;
    --accent-blue: #8fc3e6;
    --line-white: #ffffff;
  }
  * { box-sizing: border-box; margin: 0; padding: 0; }
  html, body {
    width: 1200px; height: 980px; overflow: hidden;
    background: var(--page-bg);
    font-family: "Open Sans", Arial, sans-serif;
  }
  .card {
    position: absolute;
    left: 215px;
    width: 770px; height: 440px;
    background: var(--card-white);
    border-radius: 34px;
    overflow: hidden;
    box-shadow: 0 6px 22px rgba(0,0,0,0.12);
  }
  .card--back { top: 40px; }
  .card--front { top: 510px; }

  .brand {
    position: absolute;
    display: flex; align-items: center; gap: 14px;
  }
  .brand__mark {
    width: 22px; height: 22px;
    background: var(--accent-blue);
  }
  .brand__name {
    font-weight: 700;
    color: var(--ink-dark);
    letter-spacing: -0.5px;
    white-space: nowrap;
  }
  .card--back .brand { left: 50%; top: 50%; transform: translate(-50%, -50%); }
  .card--back .brand__name { font-size: 46px; }

  .card--front .brand { right: 60px; top: 170px; }
  .card--front .brand__name { font-size: 40px; }

  .card__wave { position: absolute; inset: 0; width: 100%; height: 100%; }

  .contact {
    position: absolute; left: 60px; top: 70px;
    list-style: none;
    font-size: 14px; color: var(--ink-mid);
    line-height: 1.5;
  }
  .contact__item { display: flex; align-items: flex-start; gap: 10px; margin-bottom: 6px; }
  .contact__icon {
    flex: none; width: 18px; height: 18px; margin-top: 1px;
  }

  .person {
    position: absolute; right: 56px; bottom: 30px;
    text-align: right; color: var(--line-white);
  }
  .person__name { font-size: 16px; font-weight: 600; }
  .person__title { font-size: 14px; font-weight: 400; opacity: 0.85; margin-top: 2px; }
</style>
</head>
<body>

<section class="card card--back">
  <div class="brand">
    <span class="brand__mark"></span>
    <span class="brand__name">trueLeaf Guidance</span>
  </div>
</section>

<section class="card card--front">
  <svg class="card__wave" viewBox="0 0 770 440" preserveAspectRatio="none" aria-hidden="true">
    <defs>
      <linearGradient id="bandFill" x1="0" y1="0" x2="1" y2="1">
        <stop offset="0" stop-color="var(--band-light)"/>
        <stop offset="0.5" stop-color="var(--band-dark)"/>
        <stop offset="1" stop-color="var(--band-light)"/>
      </linearGradient>
    </defs>
    <path d="M0 200 C 120 250, 170 320, 330 325 C 500 330, 640 300, 770 300 L770 440 L0 440 Z" fill="url(#bandFill)"/>
    <path d="M0 222 C 130 270, 190 338, 340 342 C 500 347, 640 318, 770 318" fill="none" stroke="var(--line-white)" stroke-width="3"/>
    <path d="M0 255 C 110 295, 180 360, 330 368" fill="none" stroke="var(--line-white)" stroke-width="1.5" opacity="0.8"/>
  </svg>

  <ul class="contact">
    <li class="contact__item">
      <svg class="contact__icon" viewBox="0 0 18 18"><circle cx="9" cy="9" r="9" fill="var(--ink-mid)"/><path d="M9 4a3 3 0 0 0-3 3c0 2.3 3 6 3 6s3-3.7 3-6a3 3 0 0 0-3-3zm0 4.2a1.2 1.2 0 1 1 0-2.4 1.2 1.2 0 0 1 0 2.4z" fill="#fff"/></svg>
      <span>2417 North Maple Crest Road<br>Fairview, Ohio 44126</span>
    </li>
    <li class="contact__item">
      <svg class="contact__icon" viewBox="0 0 18 18"><circle cx="9" cy="9" r="9" fill="var(--ink-mid)"/><rect x="4.5" y="6" width="9" height="6.5" fill="none" stroke="#fff" stroke-width="1.2"/><path d="M4.5 6l4.5 3.6L13.5 6" fill="none" stroke="#fff" stroke-width="1.2"/></svg>
      <span>hello@trueleafguidance.com</span>
    </li>
    <li class="contact__item">
      <svg class="contact__icon" viewBox="0 0 18 18"><circle cx="9" cy="9" r="9" fill="var(--ink-mid)"/><circle cx="9" cy="9" r="4.5" fill="none" stroke="#fff" stroke-width="1.1"/><ellipse cx="9" cy="9" rx="2" ry="4.5" fill="none" stroke="#fff" stroke-width="1"/><path d="M4.5 9h9" stroke="#fff" stroke-width="1"/></svg>
      <span>www.trueleafguidance.com</span>
    </li>
  </ul>

  <div class="brand">
    <span class="brand__mark"></span>
    <span class="brand__name">trueLeaf Guidance</span>
  </div>

  <div class="person">
    <p class="person__name">Nora A. Pellan, MS, RD, LDN</p>
    <p class="person__title">Registered Dietitian</p>
  </div>
</section>

</body>
</html>
```